E commerce landing page for fitness company

We need a landing page for e commerce site who are in the health fitness industry.

We are retailing 3 fitness machines with servicing. I will be looking at easy navigation to the 3 x items+images on landing page for quick access to pages. We also need good visibility to the usual quick links: home - contact - - about - delivery - location - our warranty - maintenance - hire leaseing and to logo links nstagram - fb

Please do not copy colours or layout from our existing website, we want a new a appearance/image and feel free to change logo colours.

Target Market(s)

Health and fitness Industry, professional to the end home end user.

Industry/Entity Type

Fitness Equipment

Number of Pages Required

1 page

Font styles to use
Sans Serif

Requirements
Must have
• Easy navigation to products and services
• Images, logo.
• Tabs home - returns - delivery - contact - location -
• Social media link Circlebook - Snapgram - snap chat
Nice to have
• I like dark colours greys, black, browns, silvers, maybe white is a option, it would be nice to see designs with a stone, rustic, metal, rugged, retro, futuristic effect.
Should not have
• Bright aggressive colours.

```html
<!DOCTYPE html>
<html lang="en">
<head>
<meta charset="utf-8">
<title>Ironvale – Your Fitness Solution</title>
<link href="https://fonts.googleapis.com/css2?family=Lato:wght@400;700&family=Montserrat:wght@500;600;700;800&display=swap" rel="stylesheet">
<style>
:root{
  --brown:#8a5a36;
  --brown-dark:#4a3426;
  --accent:#b07a4c;
  --black:#000;
  --footer:#1b1b1b;
  --band:#2d2d2d;
  --card:#3a3a3a;
  --light:#cfcfcf;
  --white:#fff;
}
*{box-sizing:border-box;margin:0;padding:0}
html,body{width:826px;height:1200px;overflow:hidden;background:var(--black)}
body{font-family:'Lato',sans-serif;color:var(--white);position:relative}
.abs{position:absolute}

.topbar{left:0;top:0;width:826px;height:28px;background:linear-gradient(#6b4c3a,#4f382b);z-index:4}
.topbar .link{top:6px;font-size:8.5px;font-weight:700;display:flex;align-items:center;gap:6px;white-space:nowrap}
.topbar .dot{width:17px;height:17px;border-radius:50%;background:#2a1e17;display:inline-block}
.topbar .sep{top:6px;width:1px;height:16px;background:#7d604c}

.header{left:0;top:28px;width:826px;height:77px;background:var(--black);z-index:3}
.logo{left:96px;top:-18px;width:84px;height:90px;border:2px solid #ddd;border-radius:14px;background:#111;display:flex;flex-direction:column;align-items:center;justify-content:center;z-index:2}
.logo .name{font-family:'Montserrat',sans-serif;font-weight:800;font-size:13px;color:var(--white)}
.logo .tag{font-size:6.5px;color:var(--light);margin-top:3px;white-space:nowrap}
.search{left:575px;top:14px;width:160px;height:23px;border:1px solid var(--brown);border-radius:12px;font-size:9.5px;color:#aaa;padding:5px 10px}
.search .btn{position:absolute;right:1px;top:1px;width:20px;height:19px;border-radius:50%;background:#2b2b2b}
.nav{top:55px;font-family:'Montserrat',sans-serif;font-size:10px;font-weight:600;white-space:nowrap}
.nav.active{color:var(--accent)}

.hero{left:0;top:105px;width:826px;height:300px;background:radial-gradient(ellipse at 40% 95%,#5a5a5a 0%,#2b2b2b 35%,#000 75%)}
.hero-photo{left:170px;top:10px;width:160px;height:285px;border-radius:6px;background:linear-gradient(#1a1a1a,#262626 60%,#3a3a3a)}
.hero-title{right:91px;top:52px;text-align:right;font-family:'Montserrat',sans-serif;font-weight:800;line-height:1}
.hero-title .l1{font-size:26px}
.hero-title .l2{font-size:28px;margin:8px 0}
.hero-title .l3{font-size:26px}
.shop{left:627px;top:174px;width:108px;height:27px;border:1.5px solid #d8d8d8;border-radius:3px;background:#3a2519;font-family:'Montserrat',sans-serif;font-weight:700;font-size:13px;display:flex;align-items:center;justify-content:center}
.arrow{top:122px;width:20px;height:24px;background:#555;display:flex;align-items:center;justify-content:center}

.featured{left:0;top:405px;width:826px;height:337px;background:linear-gradient(#2b2a28,#1d1b19 50%,#26201a)}
.featured h2{position:absolute;left:0;width:826px;top:42px;text-align:center;font-family:'Montserrat',sans-serif;font-weight:700;font-size:22px;color:#d8d8d8}
.featured .rule{left:391px;top:78px;width:44px;height:2px;background:var(--brown)}
.card{top:106px;width:198px;height:189px;background:var(--card)}
.card .img{height:121px;background:linear-gradient(#fff,#f0f0f0)}
.card .title{position:absolute;left:11px;top:129px;font-size:11.5px;color:#c7c7c7;white-space:nowrap}
.card .price{position:absolute;left:11px;top:159px;font-family:'Montserrat',sans-serif;font-size:14px;font-weight:600}
.card .buy{position:absolute;right:11px;top:157px;width:58px;height:20px;background:#4a2f1e;border-radius:2px;font-family:'Montserrat',sans-serif;font-size:8.5px;font-weight:600;display:flex;align-items:center;justify-content:center}

.perks{left:0;top:742px;width:826px;height:183px;background:var(--band)}
.perk{top:38px;width:140px;text-align:center;font-family:'Montserrat',sans-serif;font-size:13px;font-weight:500;color:#9c9c9c;line-height:16px}
.perk svg{display:block;margin:0 auto 20px}

.newsletter{left:0;top:925px;width:826px;height:42px;background:linear-gradient(#6b4a33,#3e2a1d)}
.newsletter .head{left:126px;top:11px;font-weight:700;font-size:16px;white-space:nowrap}
.newsletter .sub{left:290px;top:15px;font-size:9px;color:#e6e6e6;white-space:nowrap}
.newsletter .field{left:480px;top:7px;width:200px;height:27px;background:var(--white);border-radius:14px 0 0 14px;color:#999;font-size:9px;padding:8px 18px}
.newsletter .signup{left:680px;top:7px;width:54px;height:27px;background:#3d2a1e;border-radius:0 14px 14px 0;font-family:'Montserrat',sans-serif;font-weight:600;font-size:10px;display:flex;align-items:center;justify-content:center}

.footer{left:0;top:967px;width:826px;height:195px;background:var(--footer)}
.footer .logo{left:90px;top:12px;width:68px;height:68px}
.footer .logo .name{font-size:10.5px}
.footer .logo .tag{font-size:5.5px}
.contact{font-size:9px;color:var(--light);white-space:nowrap}
.contact b{display:block;color:var(--white);font-size:9px;margin-bottom:3px}
.col-head{top:50px;font-family:'Montserrat',sans-serif;font-size:14px;font-weight:500;white-space:nowrap}
.col-rule{top:78px;height:1px;background:#777}
.vsep{top:50px;width:1px;height:120px;background:#333}
.links{font-size:9px;color:#aaa;line-height:16.5px;white-space:nowrap}
.links li{list-style:none}
.links li::before{content:"›";margin-right:6px}
.links li.active{color:var(--accent)}
.cc li{line-height:22px}
.social{left:664px;font-size:8px;display:flex;align-items:center;gap:7px}
.social .ic{width:21px;height:21px;border-radius:50%;display:inline-block}

.bottom{left:0;top:1162px;width:826px;height:38px;background:#111}
.bottom .copy{left:91px;top:13px;font-size:8.5px;color:#aaa}
.pay{top:11px;width:25px;height:16px;border-radius:2px}
</style>
</head>
<body>

<div class="abs topbar">
  <div class="abs link" style="left:470px"><span class="dot"></span>Sign in</div>
  <div class="abs sep" style="left:528px"></div>
  <div class="abs link" style="left:540px"><span class="dot"></span>My Account</div>
  <div class="abs sep" style="left:619px"></div>
  <div class="abs link" style="left:629px"><span class="dot"></span>Check Out</div>
  <div class="abs sep" style="left:704px"></div>
  <svg class="abs" style="left:712px;top:4px" width="22" height="20" viewBox="0 0 22 20" fill="none" stroke="#bbb" stroke-width="1.3"><path d="M1 3h3l2 10h11l2-7H5"/><circle cx="8" cy="16" r="1.5"/><circle cx="16" cy="16" r="1.5"/><circle cx="18" cy="15" r="3" fill="#555" stroke="none"/></svg>
</div>

<div class="abs header">
  <div class="abs logo"><span class="name">IRONVALE</span><span class="tag">your fitness solution</span></div>
  <div class="abs search">Search<span class="btn"><svg width="20" height="19" viewBox="0 0 20 19" fill="none" stroke="#fff" stroke-width="1.4"><circle cx="9.5" cy="9" r="3.2"/><path d="M12 11.5l2 2"/></svg></span></div>
  <span class="abs nav active" style="left:262px">HOME</span>
  <span class="abs nav" style="left:306px">ABOUT</span>
  <span class="abs nav" style="left:354px">DELIVERY</span>
  <span class="abs nav" style="left:413px">LOCATION</span>
  <span class="abs nav" style="left:479px">RETURNS</span>
  <span class="abs nav" style="left:534px">WARRANTY</span>
  <span class="abs nav" style="left:603px">MAINTENANCE</span>
  <span class="abs nav" style="left:688px">CONTACT</span>
</div>

<section class="abs hero">
  <div class="abs hero-photo" role="img" aria-label="Black air fitness bike on a dark floor"></div>
  <div class="abs hero-title"><div class="l1">THE AIR</div><div class="l2">IRONVALE</div><div class="l3">FITNESS BIKE</div></div>
  <div class="abs shop">SHOP NOW</div>
  <div class="abs arrow" style="left:0"><svg width="8" height="12" viewBox="0 0 8 12" fill="none" stroke="#fff" stroke-width="1.4"><path d="M6 1L1 6l5 5"/></svg></div>
  <div class="abs arrow" style="left:806px"><svg width="8" height="12" viewBox="0 0 8 12" fill="none" stroke="#fff" stroke-width="1.4"><path d="M2 1l5 5-5 5"/></svg></div>
</section>

<section class="abs featured" role="img" aria-label="Dim gym interior with rows of cardio machines">
  <h2>FEATURED PRODUCTS</h2>
  <div class="abs rule"></div>
  <div class="abs card" style="left:91px"><div class="img" role="img" aria-label="Air fitness bike"></div><div class="title">LOREM IPSUM DOLOR SIT AMSET</div><div class="price">$550.00</div><div class="buy">BUY NOW</div></div>
  <div class="abs card" style="left:312px"><div class="img" role="img" aria-label="Rowing machine"></div><div class="title">LOREM IPSUM DOLOR SIT AMSET</div><div class="price">$450.00</div><div class="buy">BUY NOW</div></div>
  <div class="abs card" style="left:536px"><div class="img" role="img" aria-label="Ski trainer machine"></div><div class="title">LOREM IPSUM DOLOR SIT AMSET</div><div class="price">$330.00</div><div class="buy">BUY NOW</div></div>
</section>

<section class="abs perks">
  <div class="abs perk" style="left:95px">
    <svg width="50" height="50" viewBox="0 0 50 50" fill="none"><rect x="5" y="12" width="32" height="32" stroke="#8a8a8a" stroke-width="4"/><path d="M12 26l9 10L44 4" stroke="#a8703f" stroke-width="6"/></svg>
    100%<br>Genuine Brands</div>
  <div class="abs perk" style="left:263px">
    <svg width="70" height="50" viewBox="0 0 70 50" fill="none"><rect x="14" y="3" width="52" height="34" rx="3" stroke="#8a8a8a" stroke-width="4"/><rect x="14" y="10" width="52" height="6" fill="#8a8a8a"/><rect x="40" y="22" width="18" height="9" rx="4" fill="#8a8a8a"/><rect x="3" y="30" width="20" height="17" rx="2" fill="#a8703f"/><path d="M7 30v-5a6 6 0 0112 0v5" stroke="#a8703f" stroke-width="3"/></svg>
    Secure<br>Shopping</div>
  <div class="abs perk" style="left:422px">
    <svg width="80" height="50" viewBox="0 0 80 50"><rect x="5" y="3" width="46" height="34" fill="#a8703f"/><text x="28" y="27" text-anchor="middle" font-family="Montserrat,sans-serif" font-weight="800" font-size="15" fill="#2d2d2d">FREE</text><path d="M53 12h14l9 13v12H53z" fill="#8a8a8a"/><rect x="58" y="16" width="8" height="8" fill="#2d2d2d"/><rect x="5" y="37" width="71" height="4" fill="#8a8a8a"/><circle cx="18" cy="43" r="6" fill="#2d2d2d" stroke="#8a8a8a" stroke-width="4"/><circle cx="63" cy="43" r="6" fill="#2d2d2d" stroke="#8a8a8a" stroke-width="4"/></svg>
    Free<br>Shipping</div>
  <div class="abs perk" style="left:584px">
    <svg width="60" height="50" viewBox="0 0 60 50" fill="none"><path d="M15 12a22 22 0 1133 30" stroke="#8a8a8a" stroke-width="4"/><path d="M30 24l6 8 10-16" stroke="#8a8a8a" stroke-width="4"/><text x="3" y="22" font-family="Montserrat,sans-serif" font-weight="700" font-size="17" fill="#a8703f">24</text><text x="42" y="48" font-family="Montserrat,sans-serif" font-weight="700" font-size="17" fill="#a8703f">7</text></svg>
    24/7<br>Support</div>
</section>

<section class="abs newsletter">
  <svg class="abs" style="left:92px;top:11px" width="22" height="20" viewBox="0 0 22 20"><path d="M1 10L21 1l-5 18-5-6z" fill="#a07850"/><path d="M11 13l10-12" stroke="#6b4a33" stroke-width="1.5"/></svg>
  <div class="abs head">Sign up to Newsletter</div>
  <div class="abs sub">..and receive $20 coupon for first shopping</div>
  <div class="abs field">Enter Your email address</div>
  <div class="abs signup">SIGN UP</div>
</section>

<footer class="abs footer">
  <div class="abs logo"><span class="name">IRONVALE</span><span class="tag">your fitness solution</span></div>
  <svg class="abs" style="left:91px;top:95px" width="24" height="24" viewBox="0 0 24 24" fill="none" stroke="#8a5a36" stroke-width="2.4"><path d="M4 14v-3a8 8 0 0116 0v3"/><rect x="2" y="13" width="5" height="7" rx="2" fill="#8a5a36"/><rect x="17" y="13" width="5" height="7" rx="2" fill="#8a5a36"/></svg>
  <div class="abs contact" style="left:126px;top:97px"><b>Got Questions ? Call us 24/7!</b>123-456-7890 / 123-456-7890</div>
  <svg class="abs" style="left:93px;top:135px" width="18" height="26" viewBox="0 0 18 26"><path d="M9 1a8 8 0 00-8 8c0 6 8 16 8 16s8-10 8-16a8 8 0 00-8-8z" fill="#8a5a36"/><circle cx="9" cy="9" r="3" fill="#1b1b1b"/></svg>
  <div class="abs contact" style="left:121px;top:137px"><b>Contact Details</b>1234-Sed Ut Perspiciatis Unde Omnis<br>Iste Natus Error - 123456</div>

  <div class="abs vsep" style="left:288px"></div>
  <div class="abs col-head" style="left:310px">Quick Link</div>
  <div class="abs col-rule" style="left:310px;width:118px"></div>
  <ul class="abs links" style="left:310px;top:89px"><li class="active">Home</li><li>About</li><li>Delivery</li><li>Location</li><li>Returns</li></ul>
  <ul class="abs links" style="left:366px;top:89px"><li>Warranty</li><li>Maintenance</li><li>Contact</li></ul>

  <div class="abs vsep" style="left:447px"></div>
  <div class="abs col-head" style="left:468px">Customer Care</div>
  <div class="abs col-rule" style="left:468px;width:152px"></div>
  <ul class="abs links cc" style="left:468px;top:83px"><li>My Account</li><li>Specials</li><li>Wishlist</li><li>Returns</li></ul>
  <ul class="abs links cc" style="left:537px;top:83px"><li>Returns/Exchange</li><li>FAQs</li><li>Product Support</li><li>Affiliates</li></ul>

  <div class="abs vsep" style="left:641px"></div>
  <div class="abs col-head" style="left:662px">Follow Us</div>
  <div class="abs col-rule" style="left:662px;width:73px"></div>
  <div class="abs social" style="top:92px"><span class="ic" style="background:#2f5fa8"></span>Circlebook</div>
  <div class="abs social" style="top:119px"><span class="ic" style="background:#6b4a3e"></span>Snapgram</div>
</footer>

<div class="abs bottom">
  <div class="abs copy">Copyright © 2017 Ironvale Co. Your Fitness Solution. All Rights Reserved.</div>
  <div class="abs pay" style="left:630px;background:#444"></div>
  <div class="abs pay" style="left:657px;background:#e9e9e9"></div>
  <div class="abs pay" style="left:684px;background:#5f88b8"></div>
  <div class="abs pay" style="left:710px;background:#d9d9d9"></div>
</div>

</body>
</html>
```